website for local kavenda practicioner and yoga teacher trainer

The website should function primarily as:
A place where people can discover Kavenda and book sessions.
A central hub connecting all of my work.
A professional home that reflects my personality and approach.
Website design for Liesbet Oonwerk — Kavenda® Structural Integration practitioner, movement educator, yoga teacher and teacher trainer.
A website that can grow with future projects.
The website should feel: Warm, Human, Invitational, Professional, Accessible, Intelligent, Calm, Clear, Playful, Exploratory, Trustworthy
Avoid: New age aesthetics, Mystical clichés, Excessive spirituality, ”Guru" vibes, Overly clinical design, Corporate wellness branding, Busy layouts
Think: modern, grounded, curious and real.
My work combines three interconnected areas:
1.Bodywork: Touch, structure, awareness and one-on-one support.
2. Movement: Yoga, Pilates and embodied movement.
3. Education: Teacher trainings, workshops and continued learning.
Underlying values:
Curiosity over certainty
Possibility over perfection
Complexity without overwhelm
Science and lived experience together
Exploration rather than dogma
Human beings before methods
The primary goal of the website is to introduce people to Kavenda® Structural Integration and make it easy for them to:
Understand what Kavenda is
Discover whether it might be relevant for them
Learn what to expect from a session
Book an appointment
Booking should always feel visible and easy.
Secondary Goal: Present all other aspects of my work in one coherent place:
Yoga classes
Pilates classes
Teacher trainings
Workshops
Retreats
One-on-one movement sessions
Collaborations with studios
Website Structure
1: HOME
1.1.Hero Section: Large welcoming image
1.2 Two Main Pathways
- Bodywork: Kavenda® Structural Integration
- Movement & Education: Yoga, Pilates, trainings, workshops and retreats
- About Preview: Small introduction with portrait. + Button:
Read More
1.3 Current Events / What's Coming Up: Upcoming trainings, workshops and retreats. (This section should be easy to update)
1.4. Contact / Newsletter: Simple contact information
2: Kavenda® Structural Integration
What is Kavenda?
For whom is it?
What does a session look like?
FAQ
Prices
Booking
Future possibility:
Kaven Movement sessions
3: Movement
- Introductory text.
- Studio Classes (link to “my home base” - > local yoga studio)
- One-to-One Sessions: booking option (this is small; not a key aspect I want to promote)
- Workshops/ Retreats / Teacher Trainings => This section should be flexible and easy to update. Visitors should be able to click into specific offerings.
4. Events
Dynamic page for: Teacher trainings, Retreats, Workshops (see section in movement; here more elaborate)
Each event should contain: Image, Short description, Location, Date, Button for more information. (Linking to hosting studio/location)
5. Work With Me
For studios, organisations and teacher training schools.
Examples: Guest teaching, Workshops, Anatomy, Sequencing, Teacher development , Continuing education -> Clear call-to-action.
Call to action!!=> Book a Session
Prominent button in the navigation.
Footer:
- About Me: Longer biography (6th page)
Personal story and background.
- Testimonials (7th page): Separate page containing testimonials from:
Kavenda clients
Students
Teacher trainees
- Contact: 8th page
Visual Direction
Natural textures. Lots of white space.Editorial feeling.Professional photography.Simple navigation.
Less "wellness influencer.” More:Thoughtful, Contemporary, Timeless, Grounded, Human
Photography should show:
Teaching
Hands-on work
Natural movement
Real interaction
Simplicity
Avoid stereotypical yoga imagery and overly spiritual aesthetics.
Keywords
Warm. Curious. Human. Professional. Embodied. Intelligent. Accessible. Playful. Grounded. Exploratory. Real.
Inspiration / Core Message
Helping people feel more at home in their bodies through touch, movement and education.
The website should communicate that these are not separate services, but different expressions of the same intention:
Bodywork • Movement • Education.
Colours:
light orange/beige: e3d5c4
light orange/off white: f9f7f3
gray azure: 556b78
orange: d07b5a
grey orange: c09f80
dark grey: 3e3e3e
dark gray cyan 2f4f4f
gray green colour: a7c4a0
Fonts: Montserrat and Poppins + raleway
In added documents a try out idea of a website + logo. I will mainly use the logo with diffrent colours (image next to text).
My audience consists of people who want to feel more at home in their bodies and who appreciate a thoughtful, grounded and human approach to movement, touch and education. (30-65yo)
wellbeing
5+ page
- montserrat, poppins, raleway

```html
<!DOCTYPE html>
<html lang="en">
<head>
<meta charset="utf-8">
<title>Liesbet Oonwerk — Yoga &amp; Bodywork</title>
<link rel="stylesheet" href="https://fonts.googleapis.com/css2?family=Montserrat:ital,wght@0,400;0,500;0,600;0,700;1,400;1,500&family=Poppins:wght@400;500&family=Raleway:wght@400;500&display=swap">
<style>
:root{
  --beige:#e3d5c4;
  --offwhite:#f9f7f3;
  --cream:#f8f3ec;
  --azure:#556b78;
  --orange:#d07b5a;
  --greyorange:#c09f80;
  --darkgrey:#3e3e3e;
  --cyan:#2f4f4f;
  --green:#a7c4a0;
  --peach:#f8e9de;
  --sage:#eeeedd;
  --sky:#e4ecf3;
  --line:#e6d6c8;
}
*{box-sizing:border-box;margin:0;padding:0}
html,body{width:1200px;height:3333px;overflow:hidden}
body{font-family:"Montserrat",sans-serif;color:var(--darkgrey);background:#fff;position:relative}
section,header,footer{position:relative;width:1200px}
.abs{position:absolute}
.btn{display:inline-flex;align-items:center;justify-content:center;font-family:"Montserrat",sans-serif;font-weight:500;text-decoration:none;border-radius:2px}
.btn-fill{background:var(--orange);color:#fff}
.btn-line{border:1.5px solid var(--orange);color:var(--orange);background:transparent}

/* hero */
.hero{height:486px;overflow:hidden}
.hero-photo{position:absolute;inset:0;background:
  radial-gradient(ellipse 380px 260px at 660px 90px,#f6d7a0 0%,rgba(233,168,96,.7) 35%,rgba(160,90,45,0) 75%),
  linear-gradient(180deg,#9c6a45 0%,#b57c4c 30%,#9a6540 55%,#6f4527 80%,#4e3020 100%)}
.nav{position:absolute;top:0;left:0;width:1200px;height:78px}
.brand{position:absolute;left:116px;top:22px;display:flex;align-items:center;gap:8px;color:#fff;font-size:23px;font-weight:500;letter-spacing:.3px}
.brand-dot{width:24px;height:24px;border-radius:50%;background:var(--darkgrey)}
.brand-sub{position:absolute;left:32px;top:28px;font-size:6px;letter-spacing:2px;color:var(--orange)}
.brand-name{color:var(--darkgrey)}
.nav-links{position:absolute;left:366px;top:30px;display:flex;gap:14px;font-size:12.5px;font-weight:500;color:var(--darkgrey)}
.nav-book{position:absolute;left:962px;top:26px;width:120px;height:26px;font-size:11.5px}
.hero-title{position:absolute;left:119px;top:172px;font-size:40px;line-height:41px;font-weight:600;color:#fff;letter-spacing:.6px}
.hero-sub{position:absolute;left:124px;top:310px;font-size:13px;line-height:17px;font-style:italic;color:#fff}
.hero-btns{position:absolute;left:126px;top:368px;display:flex;gap:22px}
.hero-btns .btn{height:28px;font-size:11.5px;padding:0 12px}
.btn-ghost{border:1.5px solid #fff;color:#fff;width:145px}

/* intention */
.intention{height:415px;text-align:center}
.section-title{font-size:36px;font-weight:500;color:var(--darkgrey);letter-spacing:.5px}
.intention .section-title{padding-top:34px}
.intention .lead{margin-top:18px;font-size:14.5px;line-height:18px;color:var(--darkgrey)}
.cards3{position:absolute;top:154px;left:90px;display:flex;gap:16px}
.card{width:326px;height:229px;text-align:left;position:relative;padding:74px 0 0 21px;border-radius:3px}
.card.peach{background:var(--peach)}
.card.sage{background:var(--sage)}
.card.sky{background:var(--sky)}
.card-icon{position:absolute;right:22px;top:18px;width:82px;height:70px;border-radius:50%}
.card h3{font-size:24px;font-weight:500;letter-spacing:.5px}
.card .tag{margin-top:10px;font-size:12.5px;font-weight:500}
.card p{margin-top:16px;font-size:12px;line-height:14px;width:290px}
.card .more{margin-top:18px;font-size:12px;color:var(--orange);display:flex;gap:22px}

/* about method */
.method{height:432px;background:var(--cream);overflow:hidden}
.method-art{position:absolute;left:0;top:0;width:569px;height:432px;background:linear-gradient(135deg,#efe7df 0%,#f6f1eb 45%,#e9dfd6 100%)}
.method-text{position:absolute;left:611px;top:50px;width:440px}
.method-text h2{font-size:31px;font-weight:500;color:var(--orange);letter-spacing:.5px}
.method-text .kicker{margin-top:12px;font-size:14.5px;font-weight:600}
.method-text .big{margin-top:36px;font-size:20px;line-height:22px;font-weight:600;width:430px}
.method-text .body{margin-top:24px;font-size:13.5px;line-height:17px;width:420px}
.method-text .btn{margin-top:18px;width:208px;height:36px;font-size:12.5px}

/* pathways */
.paths{height:520px;text-align:center}
.paths .section-title{padding-top:44px}
.paths .lead{margin-top:12px;font-size:14.5px}
.path{position:absolute;top:160px;width:474px;height:318px;border:1.5px solid var(--line);border-radius:3px;text-align:left;overflow:hidden}
.path svg{position:absolute;left:0;top:0}
.path-body{position:absolute;left:146px;top:32px;width:300px}
.path h3{font-size:25px;line-height:27px;font-weight:500;letter-spacing:.5px}
.path .desc{margin-top:18px;font-size:12.5px;line-height:17px}
.path ul{margin-top:14px;list-style:none;font-size:12.5px;line-height:19px}
.path li{display:flex;align-items:center;gap:8px}
.path li::before{content:"";width:8px;height:8px;border-radius:50%;background:var(--orange)}
.path .btn{margin-top:22px;height:28px;font-size:13px}

/* events */
.events{height:455px;background:var(--cream);text-align:center}
.events .section-title{padding-top:40px}
.event-row{position:absolute;top:1978px;}
.ev{position:absolute;top:124px;width:324px;height:216px;text-align:left;padding:24px 0 0 0}
.ev.mid{background:#fff;padding-left:17px}
.ev .date{font-size:12.5px}
.ev h4{margin-top:6px;font-size:18px;line-height:19px;font-weight:500;color:var(--orange);width:300px}
.ev .loc{margin-top:12px;font-size:10.5px;color:#777;display:flex;align-items:center;gap:6px}
.ev p{margin-top:16px;font-size:12.5px;line-height:17px;width:305px}
.ev .more{margin-top:12px;font-size:12px;color:var(--orange)}
.arrow{position:absolute;top:228px;font-size:20px;color:var(--darkgrey)}
.events .all{position:absolute;left:525px;top:376px;width:132px;height:33px;font-size:13px}

/* approach */
.approach{height:304px;text-align:center}
.approach .section-title{padding-top:40px}
.values{position:absolute;left:110px;top:128px;display:flex;gap:18px}
.value{width:148px;height:150px;border:1.5px solid var(--line);border-top:2px solid var(--greyorange);padding-top:16px;font-size:13.5px;line-height:15px}
.value svg{display:block;margin:0 auto 10px}

/* newsletter */
.newsletter{height:171px;background:var(--green);color:#fff}
.newsletter h2{position:absolute;left:113px;top:40px;font-size:37px;font-weight:600;letter-spacing:.8px}
.newsletter p{position:absolute;left:114px;top:98px;font-size:14.5px;line-height:18px}
.newsletter .btn{position:absolute;left:685px;top:53px;width:314px;height:61px;font-size:26px;font-weight:600;gap:18px;letter-spacing:.6px}

/* footer */
.closing{height:550px;color:#fff;overflow:hidden}
.closing-photo{position:absolute;inset:0;background:linear-gradient(180deg,#4b4b4b 0%,#545454 40%,#4a4744 75%,#3f3b37 100%)}
.closing h2{position:absolute;left:0;width:1200px;top:56px;text-align:center;font-size:44px;font-weight:500;letter-spacing:1px}
.closing .lead{position:absolute;left:0;width:1200px;top:122px;text-align:center;font-size:15px;line-height:20px}
.closing .ctas{position:absolute;left:444px;top:212px;display:flex;gap:13px}
.closing .ctas .btn{width:150px;height:28px;font-size:10.5px;letter-spacing:.5px}
.btn-white{background:#fff;color:var(--darkgrey)}
.foot-brand{position:absolute;left:116px;top:340px;display:flex;align-items:center;gap:10px;font-size:30px;font-weight:500}
.foot-brand .brand-dot{width:36px;height:36px;background:#fff}
.social{position:absolute;left:232px;top:396px;display:flex;gap:10px}
.social span{width:14px;height:14px;border-radius:50%;border:1.5px solid #fff}
.fcol{position:absolute;top:300px;font-size:10px;line-height:15.5px}
.fcol h5{font-size:11px;font-weight:500;letter-spacing:.8px;margin-bottom:18px}
.contact-line{display:flex;align-items:center;gap:14px;margin-top:12px}
.copyright{position:absolute;left:0;width:1200px;top:492px;text-align:center;font-size:11px;font-weight:500}
</style>
</head>
<body>

<header class="hero">
  <div class="hero-photo" role="img" aria-label="Photograph of a woman in a low lunge with hands at her chest on a beach at sunset"></div>
  <nav class="nav">
    <div class="brand"><span class="brand-dot"></span><span class="brand-name">Liesbet Oonwerk</span></div>
    <div class="nav-links"><span>Kavenda® Structural Integration</span><span>Movement</span><span>Events</span><span>Work With Me</span><span>About</span><span>Contact</span></div>
    <a class="btn btn-fill nav-book">Book a Session</a>
  </nav>
  <h1 class="hero-title">Helping People Feel<br>More At Home In<br>Their Bodies</h1>
  <p class="hero-sub">Kavenda® Structural Integration, movement education, yoga,<br>Pilates, workshops and teacher trainings.</p>
  <div class="hero-btns"><a class="btn btn-fill">Book a Session</a><a class="btn btn-ghost">Explore My Work</a></div>
</header>

<section class="intention">
  <h2 class="section-title">One Intention. Three Expressions.</h2>
  <p class="lead">They are different ways of supporting people in feeling more connected, capable<br>and at home in their bodies.</p>
  <div class="cards3">
    <article class="card peach">
      <div class="card-icon" role="img" aria-label="Icon of a person with arms raised" style="background:var(--orange)"></div>
      <h3>Bodywork</h3><div class="tag">Kavenda® Structural Integration</div>
      <p>Hands-on support for posture movement and awareness.</p>
      <div class="more">Learn About Kavenda <span>›</span></div>
    </article>
    <article class="card sage">
      <div class="card-icon" role="img" aria-label="Icon of a person in a yoga pose" style="background:#9fae84"></div>
      <h3>Movement</h3><div class="tag">Yoga • Pilates • One-to-One Movement</div>
      <p>Embeded, movement practices for strength, mobility and ease.</p>
      <div class="more">Explore Movement <span>›</span></div>
    </article>
    <article class="card sky">
      <div class="card-icon" role="img" aria-label="Icon of an open book with a light bulb" style="background:#3f5556"></div>
      <h3>Education</h3><div class="tag">Teacher Trainings • Workshops</div>
      <p>Learn, explore and grow trhough education and shared experience.</p>
      <div class="more">View Events <span>›</span></div>
    </article>
  </div>
</section>

<section class="method">
  <div class="method-art" role="img" aria-label="Line drawing of a woman's upper body holding out one hand, over soft stone textures"></div>
  <div class="method-text">
    <h2>What Is Kavenda?</h2>
    <div class="kicker">Curious About Kavenda® Structural Integration?</div>
    <p class="big">Kavenda is a hands-on approach that works with posture, movement, awareness and the body's relationship with gravity.</p>
    <p class="body">Whether you are experiencing discomfort, seeking greater ease of movement or simply wanting to understand your body better, Kavenda offers a process of exploration and change.</p>
    <a class="btn btn-line">Learn More About Kavenda</a>
  </div>
</section>

<section class="paths">
  <h2 class="section-title">How Would You Like To Begin?</h2>
  <p class="lead">Choose the path that feels most relevant for you right now.</p>
  <article class="path" style="left:110px">
    <svg width="120" height="318" viewBox="0 0 120 318"><path d="M0 0H50C95 40 60 90 70 130C80 190 125 220 95 265C80 290 40 300 0 318V135A30 30 0 0 0 0 75Z" fill="var(--greyorange)"/></svg>
    <div class="path-body">
      <h3>Kavenda® Structural Integration</h3>
      <p class="desc">Understand what it isLearn what to expect<br>Discover if it is right for you</p>
      <ul><li>What is Kavenda?</li><li>What happens in a session</li><li>Prices a FAQ</li><li>Book an Appointment</li></ul>
      <a class="btn btn-line" style="width:115px">Start Here →</a>
    </div>
  </article>
  <article class="path" style="left:610px">
    <svg width="120" height="318" viewBox="0 0 120 318"><path d="M0 70C30 55 60 45 95 45C85 90 85 150 98 210C108 260 100 300 70 318H0Z" fill="var(--orange)"/></svg>
    <div class="path-body">
      <h3>Monvement &amp;<br>Education</h3>
      <p class="desc">Explore classes, workshops,retreats<br>and trainings</p>
      <ul><li>Yoga &amp; Pilates Classes</li><li>One-to-One Movement</li><li>Workshops &amp; Retreats</li><li>Teacher Training</li></ul>
      <a class="btn btn-line" style="width:115px">Explore →</a>
    </div>
  </article>
</section>

<section class="events">
  <h2 class="section-title">What's Coming Up</h2>
  <span class="arrow" style="left:72px">‹</span>
  <article class="ev" style="left:111px">
    <div class="date">12–14 September 2026</div>
    <h4>Embodied Anatomy for Yoga Teachers</h4>
    <div class="loc"><svg width="11" height="13" viewBox="0 0 11 13"><path d="M5.5 12S1 7.5 1 5a4.5 4.5 0 0 1 9 0c0 2.5-4.5 7-4.5 7Z" fill="none" stroke="#777"/><circle cx="5.5" cy="5" r="1.6" fill="none" stroke="#777"/></svg>Amsterdam, Netherlands</div>
    <p>Explore anatomy through movement, touch and lived experience.</p>
    <div class="more">Learn More ›</div>
  </article>
  <article class="ev mid" style="left:435px">
    <div class="date">23–27 October 2026</div>
    <h4>Move, Rest &amp; Reconnect Retreat</h4>
    <div class="loc"><svg width="11" height="13" viewBox="0 0 11 13"><path d="M5.5 12S1 7.5 1 5a4.5 4.5 0 0 1 9 0c0 2.5-4.5 7-4.5 7Z" fill="none" stroke="#777"/><circle cx="5.5" cy="5" r="1.6" fill="none" stroke="#777"/></svg>Ardennes, Belgium</div>
    <p>A nourishing retreat combining movement, restorative practices and time in nature.</p>
    <div class="more">Learn More ›</div>
  </article>
  <article class="ev" style="left:790px">
    <div class="date">15 November 2026</div>
    <h4>Movement, Posture &amp; Every-day Ease</h4>
    <div class="loc"><svg width="11" height="13" viewBox="0 0 11 13"><path d="M5.5 12S1 7.5 1 5a4.5 4.5 0 0 1 9 0c0 2.5-4.5 7-4.5 7Z" fill="none" stroke="#777"/><circle cx="5.5" cy="5" r="1.6" fill="none" stroke="#777"/></svg>Utrecht, Netherlands</div>
    <p>Discover how movement habits influence posture, comfort and resilience.</p>
    <div class="more">Learn More ›</div>
  </article>
  <span class="arrow" style="left:1112px">›</span>
  <a class="btn btn-line all">View All Events</a>
</section>

<section class="approach">
  <h2 class="section-title">How I Approach My Work</h2>
  <div class="values">
    <div class="value"><svg width="80" height="60" viewBox="0 0 80 60" fill="none" stroke="var(--orange)" stroke-width="2"><path d="M8 34C20 18 50 18 62 34C50 50 20 50 8 34Z"/><circle cx="35" cy="34" r="8"/><circle cx="60" cy="16" r="10"/><path d="M57 13a3 3 0 1 1 4 3v3M60 22v1"/></svg>Curiosity Over<br>Certainty</div>
    <div class="value"><svg width="80" height="60" viewBox="0 0 80 60" fill="none" stroke="var(--orange)" stroke-width="2"><rect x="12" y="10" width="26" height="44"/><path d="M20 54V18M30 54V18"/><path d="M52 14h16v10a8 8 0 0 1-16 0Z"/><path d="M60 32v12M54 46h12"/></svg>Possibility Over<br>Perfection</div>
    <div class="value"><svg width="80" height="60" viewBox="0 0 80 60" fill="none" stroke="var(--orange)" stroke-width="2"><circle cx="40" cy="36" r="20"/><path d="M34 10h12M37 10v8M43 10v8"/><path d="M22 38h36"/></svg>Science &amp; Lived<br>Experience</div>
    <div class="value"><svg width="80" height="60" viewBox="0 0 80 60" fill="none" stroke="var(--orange)" stroke-width="2"><circle cx="40" cy="12" r="5"/><path d="M33 22h14v16h-3v16h-8V38h-3Z"/><path d="M18 34a22 22 0 0 1 8-20M62 30a22 22 0 0 1-8 20"/></svg>Human<br>Beings Before<br>Methods</div>
    <div class="value"><svg width="80" height="60" viewBox="0 0 80 60" fill="none" stroke="var(--orange)" stroke-width="2"><circle cx="40" cy="30" r="24"/><circle cx="40" cy="12" r="4"/><circle cx="24" cy="36" r="4"/><circle cx="56" cy="36" r="4"/><path d="M40 16L26 33M40 16l14 17M28 36h24"/></svg>Complexity<br>Without<br>Overwhelm</div>
    <div class="value"><svg width="80" height="60" viewBox="0 0 80 60" fill="none" stroke="var(--orange)" stroke-width="2"><circle cx="40" cy="30" r="24"/><path d="M28 42l6-18 18-6-6 18Z"/></svg>Exploration<br>Rather Than<br>Dogma</div>
  </div>
</section>

<section class="newsletter">
  <h2>Stay Connected</h2>
  <p>Receive updates about trainings, workshops,<br>retreats and new offerings.</p>
  <a class="btn btn-fill">Subscribe Now <svg width="28" height="28" viewBox="0 0 28 28" fill="none" stroke="#fff" stroke-width="3"><path d="M4 24L24 4M8 4h16v16"/></svg></a>
</section>

<footer class="closing">
  <div class="closing-photo" role="img" aria-label="Dim photograph of a person stretching one leg high, darkened behind the footer"></div>
  <h2>Ready To Explore What's Possible?</h2>
  <p class="lead">Whether through bodywork, movement or education, the goal is the same:<br>helping you feel more at home in your body.</p>
  <div class="ctas"><a class="btn btn-fill">BOOK A SESSION</a><a class="btn btn-white">GET IN TOUCH</a></div>
  <div class="foot-brand"><span class="brand-dot"></span>Liesbet Oonwerk</div>
  <div class="social" aria-label="Social profiles"><span></span><span></span></div>
  <div class="fcol" style="left:440px"><h5>NAVIGATION</h5>Home<br>Kavenda® Structural Integration<br>Movement<br>Events<br>Work With Me<br>About<br>Testimonials<br>Contact</div>
  <div class="fcol" style="left:665px"><h5>OUR INTENTION</h5>Bodywork<br>Movement<br>Education</div>
  <div class="fcol" style="left:876px;top:297px"><h5>CONTACT US</h5>
    <div class="contact-line" style="font-size:17px"><svg width="16" height="16" viewBox="0 0 16 16"><path d="M3 1l3 3-2 2c1 2 3 4 5 5l2-2 3 3-2 3C6 15 1 10 1 3Z" fill="#fff"/></svg>0049 170 555 01 84</div>
    <div class="contact-line" style="font-size:11.5px;margin-top:8px"><svg width="18" height="12" viewBox="0 0 18 12" fill="none" stroke="#fff" stroke-width="1.5"><rect x="1" y="1" width="16" height="10"/><path d="M1 1l8 6 8-6"/></svg>hello@oonwerkpractice.com</div>
  </div>
  <p class="copyright">Copyright © 2026 oonwerkpractice.com</p>
</footer>

</body>
</html>
```